タイトル 「週末ガーデナーのための水やり流・花咲かせ節約術」
サブタイトル 「毎日が楽になる5つの習慣」

上記の表紙デザインをお願いします。基本お任せします。
本の内容  原稿を添付します。

その他ご不明な点がございましたらお気楽にご質問ください。よろしくお願いいたします。
著者名 星空ナビゲーター 森川佳代 from神戸

本の内容とよくマッチしたデザインだと思いました。インパクトもあり本の対象であるアラフォーの好みと合っているように思いました。

沢山のご応募ありがとうございました。何もかもか初めての作業で、不安でしたが、関心を持っていただいて心からありがたく思っております。これからも電子書籍の出版を考えております。ご縁がありましたらまた、今後もよろしくお願いします。
ありがとうございました。

```html
<!DOCTYPE html>
<html lang="ja">
<head>
<meta charset="UTF-8">
<title>週末ガーデナーのための水やり流・花咲かせ節約術</title>
<link href="https://fonts.googleapis.com/css2?family=Zen+Maru+Gothic:wght@500;700&family=Zen+Kaku+Gothic+New:wght@500;700;900&family=Playfair+Display:ital,wght@1,700&display=swap" rel="stylesheet">
<style>
  :root {
    --paper: #fbfbfa;
    --ink: #1c1c1c;
    --rose: #e2508c;
    --rose-band: #f39ac4;
    --rose-frame: #fbd3e6;
    --gold: #d9a93a;
    --gold-light: #f3d57a;
    --author: #3a3a3a;
    --sky: #f6f7f6;
    --sea: #cfe3ea;
    --sand: #e9e4dc;
  }
  * { margin: 0; padding: 0; box-sizing: border-box; }
  html, body { width: 750px; height: 1200px; overflow: hidden; background: var(--paper); }
  .cover {
    position: relative;
    width: 750px;
    height: 1200px;
    overflow: hidden;
    font-family: "Zen Kaku Gothic New", sans-serif;
  }
  .cover-photo {
    position: absolute;
    inset: 0;
    background: linear-gradient(180deg, #fdfdfc 0%, var(--sky) 22%, #e6eef0 38%, var(--sea) 52%, #dbe8ec 62%, var(--sand) 78%, #f1efeb 100%);
  }
  .series-line {
    position: absolute;
    left: 0; right: 0;
    text-align: center;
    font-family: "Zen Maru Gothic", sans-serif;
    font-weight: 500;
    color: var(--rose);
    font-size: 40px;
    line-height: 1;
    letter-spacing: 0.14em;
  }
  .series-line.first { top: 30px; }
  .series-line.second { top: 92px; }
  .main-title {
    position: absolute;
    top: 178px; left: 0; right: 0;
    text-align: center;
    font-weight: 900;
    font-size: 82px;
    line-height: 1;
    letter-spacing: 0.06em;
    color: var(--ink);
  }
  .subtitle-lead {
    position: absolute;
    right: 48px;
    top: 378px;
    font-size: 32px;
    line-height: 1;
    font-weight: 500;
    letter-spacing: 0.06em;
    color: var(--ink);
  }
  .subtitle-main {
    position: absolute;
    right: 44px;
    top: 408px;
    font-size: 60px;
    font-weight: 700;
    line-height: 100px;
    letter-spacing: 0.04em;
    color: var(--ink);
  }
  .subtitle-number {
    font-family: "Playfair Display", serif;
    font-style: italic;
    font-weight: 700;
    font-size: 112px;
    color: var(--gold);
    text-shadow: 0 0 6px var(--gold-light), 0 2px 0 #fff;
    margin-right: 4px;
  }
  .author {
    position: absolute;
    left: 430px;
    top: 520px;
    color: var(--author);
    font-weight: 500;
    font-size: 27px;
    line-height: 54px;
    letter-spacing: 0.04em;
  }
  .promise {
    position: absolute;
    left: 20px; right: 20px;
    top: 968px;
    height: 206px;
    background: var(--rose-band);
    padding: 10px;
  }
  .promise-frame {
    width: 100%;
    height: 100%;
    border: 3px solid var(--rose-frame);
    display: flex;
    flex-direction: column;
  }
  .promise-headline {
    flex: 0 0 104px;
    display: flex;
    align-items: center;
    justify-content: center;
    color: #fff;
    font-weight: 700;
    font-size: 48px;
    letter-spacing: 0.06em;
  }
  .promise-tagline {
    flex: 1;
    background: #fff;
    display: flex;
    align-items: center;
    justify-content: center;
    color: var(--rose);
    font-weight: 500;
    font-size: 30px;
    letter-spacing: 0.03em;
  }
</style>
</head>
<body>
  <main class="cover">
    <div class="cover-photo" role="img" aria-label="淡い空と海辺の砂浜の写真"></div>

    <p class="series-line first">週末ガーデナーのための</p>
    <p class="series-line second">水やり流</p>
    <h1 class="main-title">花咲かせ節約術</h1>

    <p class="subtitle-lead">毎日が楽になる</p>
    <p class="subtitle-main"><span class="subtitle-number">5</span>つの習慣</p>

    <p class="author">星空ナビゲーター<br>森川佳代 from 神戸</p>

    <section class="promise">
      <div class="promise-frame">
        <p class="promise-headline">忙しい週末でも花咲く庭</p>
        <p class="promise-tagline">を手に入れ“今が一番楽しい”と言うための方法</p>
      </div>
    </section>
  </main>
</body>
</html>
```